The most modern business card ever !!!

Our company call “Vantilo”. Vantilo is a technology company specialized in cruises solutions. Out main product is a platform to reserve cruises. This is a revolutionary platform that make easier to travel agencies and final users to reserve cruises across dozen companies like tarvik, welbi, dpv, hbt, etc..We are a “start up”, with a young team of developers and we want to transmit it.. For it, we want something different, a modern business card that represent cruises and technology.. When someone receive this card, this person should say: wowww this is different… this is modern… this is a cruise related company..
Contact Information for Business Card
Requirements
Must have
- diferent, modern
Should not have
- traditions business card

```html
<!DOCTYPE html>
<html lang="en">
<head>
<meta charset="utf-8">
<title>Vantilo Business Card</title>
<link href="https://fonts.googleapis.com/css2?family=Montserrat:wght@400;500;600&display=swap" rel="stylesheet">
<style>
  :root {
    --canvas: #e4e5e7;
    --card: #1b1b1d;
    --card-back: #19191a;
    --accent: #1fa3e0;
    --ink: #f2f2f2;
    --ink-soft: #d8d8d8;
    --emboss: #3a3a3d;
  }
  * { margin: 0; padding: 0; box-sizing: border-box; }
  html, body {
    width: 1200px; height: 900px; overflow: hidden;
    background: var(--canvas);
    font-family: "Montserrat", sans-serif;
  }
  .canvas {
    position: relative; width: 1200px; height: 900px;
    display: flex; flex-direction: column; align-items: center; justify-content: center; gap: 44px;
  }
  .card {
    position: relative; width: 660px; height: 377px;
    box-shadow: 0 10px 28px rgba(0,0,0,0.22);
  }
  .card-front {
    background: var(--card);
    border-left: 5px solid var(--accent);
    border-bottom: 5px solid var(--accent);
  }
  .brand {
    position: absolute; top: 44px; right: 46px;
    font-weight: 500; font-size: 58px; letter-spacing: 1px;
    color: var(--ink); line-height: 1;
  }
  .divider {
    position: absolute; left: 60px; right: 46px; top: 214px;
    height: 1px; background: var(--accent);
  }
  .person {
    position: absolute; left: 60px; top: 156px;
  }
  .person-name {
    font-weight: 600; font-size: 24px; letter-spacing: 1.5px;
    color: var(--accent); text-transform: uppercase;
  }
  .person-role {
    margin-top: 4px; font-size: 15px; letter-spacing: 1px; color: var(--ink);
  }
  .address {
    position: absolute; right: 46px; top: 158px; text-align: right;
    font-size: 15px; letter-spacing: 1.2px; line-height: 1.6; color: var(--ink-soft);
  }
  .contacts {
    position: absolute; left: 60px; top: 244px; list-style: none;
    font-size: 15px; letter-spacing: 1.2px; line-height: 1.75; color: var(--ink-soft);
  }
  .contacts li { display: flex; align-items: center; gap: 10px; }
  .contacts svg { width: 13px; height: 13px; fill: var(--accent); flex-shrink: 0; }
  .card-back {
    background: var(--card-back);
    display: flex; align-items: center; justify-content: center;
  }
  .brand-emboss {
    font-weight: 500; font-size: 104px; letter-spacing: 2px;
    color: var(--emboss); line-height: 1;
  }
</style>
</head>
<body>
<main class="canvas">
  <section class="card card-front">
    <div class="brand">Vantilo</div>
    <div class="person">
      <h1 class="person-name">Daniel Reyes</h1>
      <p class="person-role">Director</p>
    </div>
    <address class="address">412b Harbor Lane,<br>Wellport, NZ, 4021</address>
    <div class="divider"></div>
    <ul class="contacts">
      <li><svg viewBox="0 0 24 24" aria-hidden="true"><path d="M6.6 10.8a15 15 0 0 0 6.6 6.6l2.2-2.2a1 1 0 0 1 1-.25 11.4 11.4 0 0 0 3.6.57 1 1 0 0 1 1 1V20a1 1 0 0 1-1 1A17 17 0 0 1 3 4a1 1 0 0 1 1-1h3.5a1 1 0 0 1 1 1c0 1.25.2 2.45.57 3.57a1 1 0 0 1-.25 1z"/></svg>(555) 210-4471</li>
      <li><svg viewBox="0 0 24 24" aria-hidden="true"><path d="M3 5h18v14H3z M3 5l9 7 9-7" fill="none" stroke="#1fa3e0" stroke-width="2.4"/></svg>info@vantilo.com.br</li>
      <li><svg viewBox="0 0 24 24" aria-hidden="true"><circle cx="12" cy="12" r="9" fill="none" stroke="#1fa3e0" stroke-width="2.4"/><path d="M3 12h18M12 3c3 3 3 15 0 18M12 3c-3 3-3 15 0 18" fill="none" stroke="#1fa3e0" stroke-width="1.8"/></svg>www.vantilo.com.br</li>
    </ul>
  </section>
  <section class="card card-back">
    <div class="brand-emboss">Vantilo</div>
  </section>
</main>
</body>
</html>
```